Beauty & Wellness business needs a flyer to describe a multitude of therapy

I would like a flyer to represent my company. i would like it to have the form of a pamphlet 6 pages. The flyer should be in french if possible, but english also is okay. I'll upload a word file that illustrate what i would like, but it can be of course other images, this is just an example. And the text includes all the services we provide, some small description might be added if you think it's worth it from design point of view.
Target Market(s)
The market is seasonal. it's mostly winter for skiers, so wealthy and sporty people, and attentive to nature. But i also want to promote the brand for locals all year long, with reasonable pricing.
Industry/Entity Type
Wellness & aesthetics
Look and feel

```html
<!DOCTYPE html>
<html lang="fr">
<head>
<meta charset="utf-8">
<title>Aveline – Dépliant extérieur</title>
<link rel="stylesheet" href="https://fonts.googleapis.com/css2?family=Montserrat:wght@400;500;800&display=swap">
<style>
  :root{
    --backdrop:#6f747b;
    --paper:#f4f4f5;
    --paper-shade:#dcdcde;
    --plum:#7a1c66;
    --plum-deep:#5e1250;
    --gold:#c8ad72;
    --olive:#8c8a4e;
    --ink:#141414;
    --white:#ffffff;
    --skin-light:#f1d8c6;
    --skin-mid:#d9a98c;
  }
  *{margin:0;padding:0;box-sizing:border-box}
  html,body{width:1200px;height:2441px;overflow:hidden;background:var(--backdrop)}
  body{font-family:"Montserrat",Arial,sans-serif;position:relative}
  .brochure-outside{
    position:absolute;left:30px;top:803px;width:1140px;height:835px;overflow:hidden;
    background:linear-gradient(135deg,var(--white) 0%,var(--paper) 45%,var(--paper-shade) 100%);
  }
  .brochure-outside svg{position:absolute;left:0;top:0}
  .panel-title{position:absolute;font-weight:800;font-size:31px;line-height:39px;text-transform:uppercase;letter-spacing:.5px}
  .massages-title{left:47px;top:62px;color:var(--ink)}
  .massage-list{position:absolute;left:40px;top:188px;list-style:none}
  .massage-list li{font-size:22.5px;font-weight:500;color:#262626;height:37.5px;padding-left:40px;position:relative;letter-spacing:.3px;white-space:nowrap}
  .massage-list li::before{content:"";position:absolute;left:0;top:7px;width:21px;height:21px;border-radius:50%;background:var(--ink)}
  .facial-title{left:500px;top:248px;color:var(--white)}
  .facial-list{position:absolute;left:498px;top:0;list-style:none;color:var(--white);font-size:22px;font-weight:500;letter-spacing:.4px}
  .facial-list li{position:absolute;left:0;white-space:nowrap;line-height:28px}
  .brand{position:absolute;left:900px;top:55px;width:220px;text-align:center}
  .brand-mark{width:96px;height:96px;border-radius:50%;border:4px solid var(--plum);margin:0 auto 22px}
  .brand-name{font-weight:800;font-size:30px;letter-spacing:4px;color:var(--plum);text-transform:uppercase}
</style>
</head>
<body>
<main class="brochure-outside">
  <svg width="1140" height="835" viewBox="0 0 1140 835">
    <defs>
      <linearGradient id="plumFill" x1="0" y1="0" x2="1" y2="1">
        <stop offset="0" stop-color="var(--plum)"/>
        <stop offset="1" stop-color="var(--plum-deep)"/>
      </linearGradient>
      <radialGradient id="skinTone" cx=".5" cy=".45" r=".6">
        <stop offset="0" stop-color="var(--skin-light)"/>
        <stop offset="1" stop-color="var(--skin-mid)"/>
      </radialGradient>
    </defs>
    <path class="gold-ribbon" d="M655,0 L720,0 C565,80 460,260 420,455 C385,620 340,715 262,835 L240,835 C300,720 360,620 395,450 C440,250 540,70 655,0 Z" fill="var(--gold)"/>
    <path class="plum-wave" d="M700,0 L975,0 C885,60 845,190 845,280 C845,360 775,385 775,475 C775,560 805,640 735,705 C685,750 650,800 640,835 L262,835 C340,715 385,620 420,455 C460,260 565,80 700,0 Z" fill="url(#plumFill)"/>
    <path class="guide-line" d="M560,120 C470,230 430,380 400,560 C380,680 340,760 310,835" fill="none" stroke="var(--gold)" stroke-width="1.5" stroke-dasharray="6 5"/>
    <g class="list-connectors" stroke="var(--gold)" stroke-width="1.5" stroke-dasharray="5 4" fill="var(--olive)">
      <line x1="418" y1="390" x2="435" y2="390"/><circle cx="435" cy="390" r="5" stroke="none"/>
      <line x1="400" y1="478" x2="435" y2="478"/><circle cx="435" cy="478" r="5" stroke="none"/>
      <line x1="393" y1="533" x2="435" y2="533"/><circle cx="435" cy="533" r="5" stroke="none"/>
      <line x1="385" y1="588" x2="435" y2="588"/><circle cx="435" cy="588" r="5" stroke="none"/>
      <line x1="370" y1="643" x2="435" y2="643"/><circle cx="435" cy="643" r="5" stroke="none"/>
      <line x1="345" y1="697" x2="435" y2="697"/><circle cx="435" cy="697" r="5" stroke="none"/>
      <line x1="300" y1="752" x2="435" y2="752"/><circle cx="435" cy="752" r="5" stroke="none"/>
    </g>
    <circle cx="580" cy="107" r="100" fill="var(--white)"/>
    <circle cx="580" cy="107" r="93" fill="url(#skinTone)" role="img" aria-label="Photo : visage avec masque de soin appliqué"/>
    <circle cx="135" cy="780" r="150" fill="var(--plum)"/>
    <circle cx="135" cy="780" r="142" fill="url(#skinTone)" role="img" aria-label="Photo : cliente recevant un soin du visage"/>
    <path d="M640,835 C660,760 700,720 760,700 C790,560 820,420 900,360 C980,310 1080,320 1140,370 L1140,835 Z" fill="url(#skinTone)" role="img" aria-label="Photo : portrait d'une femme à la peau lumineuse"/>
  </svg>

  <h2 class="panel-title massages-title">Nos<br>massages<br>maisons</h2>
  <ul class="massage-list">
    <li>Aryuvédique Pindas</li>
    <li>Pour femmes enceintes</li>
    <li>Drainage lymphatique</li>
    <li>Méso Cellulite</li>
    <li>Réflexologie</li>
    <li>Relaxant</li>
    <li>Pierre chaude</li>
    <li>Bambou</li>
    <li>Guasha</li>
    <li>Deep tissue</li>
    <li>Sportif</li>
    <li>Shiatsu</li>
  </ul>

  <h2 class="panel-title facial-title">Nos<br>traitements<br>du visage</h2>
  <ul class="facial-list">
    <li style="top:372px">Soin du<br>visage classique</li>
    <li style="top:463px">Fils de collagènes</li>
    <li style="top:518px">Thérapie au plâtre</li>
    <li style="top:573px">Plasma Lift</li>
    <li style="top:628px">Chromothérapie</li>
    <li style="top:682px">Aromathérapie</li>
    <li style="top:737px">Needling</li>
  </ul>

  <div class="brand">
    <div class="brand-mark"></div>
    <div class="brand-name">Aveline</div>
  </div>
</main>
</body>
</html>
```